KTR Builders
Home Page
Project: KTR Builders
KTR Builders  -
Creative Brief
www.ktrbuilders.com
KTR Builders is a residential general contractor. We build new custom homes, house additions, bathroom and kitchen remodeling.
We also can do medium size commercial buildings and office space buildout.
KTR Builders is also trained installer of the Brindell Pools.
We Need template of the home page and design of the sub pages.
yellow
Verdana, Trebuchet MS, Georgia

```html
<!DOCTYPE html>
<html lang="en">
<head>
<meta charset="utf-8">
<title>KTR Builders – Home</title>
<link rel="stylesheet" href="https://fonts.googleapis.com/css2?family=Open+Sans:wght@400;600;700&family=Noto+Serif:wght@400;700&family=Caveat:wght@500&display=swap">
<style>
  :root{
    --navy:#1f4a8c;
    --navy-dark:#163a6e;
    --tab:#6b6b6b;
    --yellow:#f2d200;
    --gray-bg:#eeeeee;
    --panel:#f6f6f6;
    --line:#d6d6d6;
    --text:#555;
    --white:#fff;
  }
  *{box-sizing:border-box;margin:0;padding:0}
  html,body{width:1200px;height:1042px;overflow:hidden;background:var(--white)}
  body{position:relative;font-family:"Open Sans",Verdana,sans-serif;color:var(--text);font-size:11px;line-height:1.45}
  .abs{position:absolute}

  /* header */
  .main-nav{left:493px;top:0;display:flex;gap:4px}
  .main-nav a{display:block;height:22px;padding:0 14px;line-height:22px;color:var(--white);background:var(--tab);font-size:11px;font-weight:700;text-decoration:none;border-radius:0 0 6px 6px;text-transform:uppercase}
  .main-nav a.active{background:var(--navy);padding:0 28px}
  .brand{left:212px;top:56px;display:flex;align-items:center;gap:12px}
  .brand-dot{width:26px;height:26px;border-radius:50%;background:var(--navy);display:block}
  .brand-name{font-family:"Open Sans",sans-serif;font-weight:400;color:var(--navy);font-size:30px;line-height:1;white-space:nowrap}
  .motto{left:790px;top:40px;width:215px;font-family:"Caveat",cursive;font-size:20px;line-height:1.05;color:#444}
  .motto cite{display:block;text-align:right;font-style:normal;font-size:15px;margin-top:3px}
  .header-rule{left:0;top:132px;width:1200px;height:4px;background:linear-gradient(90deg,transparent,var(--yellow) 20%,var(--yellow) 80%,transparent)}

  /* slider */
  .slider{left:203px;top:147px;width:797px;height:333px;background:#d8d8d8;padding:6px}
  .slide-photo{width:100%;height:100%;background:linear-gradient(135deg,#e8e4dc 0%,#cfc7b6 45%,#b99a6e 75%,#8b3b2c 100%)}
  .slide-caption{left:99px;top:6px;width:234px;height:321px;background:rgba(255,255,255,.82);padding:40px 14px 0}
  .slide-caption h2{font-family:"Noto Serif",Georgia,serif;font-size:20px;color:#555;text-transform:uppercase}
  .slide-caption h3{font-size:10px;font-style:italic;color:#444;margin-bottom:36px}
  .slide-caption p{font-size:10px;color:#777}
  .btn{display:inline-block;background:var(--navy);color:var(--white);border-radius:12px;padding:5px 20px;font-family:"Noto Serif",Georgia,serif;font-size:12px}
  .slide-caption .btn{position:absolute;left:14px;bottom:36px}
  .dots{right:12px;bottom:10px;display:flex;gap:4px}
  .dots i{width:13px;height:13px;background:var(--white);display:block}
  .dots i.on{background:var(--yellow)}

  /* content row */
  .testimonials{left:203px;top:502px;width:262px;height:200px;background:var(--panel);border:1px solid var(--line);padding:10px 12px}
  .testimonials h2{font-size:15px;font-weight:700;color:var(--navy);text-transform:uppercase;border-bottom:1px solid var(--line);padding-bottom:8px;margin-bottom:8px}
  .testimonials p{font-size:9.5px}
  .testimonials .author{font-weight:700;color:#444;margin-top:6px}
  .about{left:480px;top:502px;width:335px}
  .about h2{font-family:"Noto Serif",Georgia,serif;color:var(--navy);font-size:19px;font-weight:400;margin-bottom:10px}
  .about-img{float:left;width:100px;height:78px;margin:0 10px 6px 0;background:linear-gradient(160deg,#c9c9c9,#8a6a4a)}
  .about p{font-size:9.5px;margin-bottom:6px}
  .about .hl{color:var(--navy);font-style:italic;font-weight:600}
  .showcase{left:832px;top:508px;width:168px;height:192px;border:1px solid var(--line);padding:8px;background:var(--white)}
  .showcase-img{width:100%;height:100%;border:4px solid var(--yellow);background:linear-gradient(180deg,#b0182a,#7a0c18)}
  .showcase span{position:absolute;left:8px;right:8px;bottom:8px;height:28px;line-height:28px;text-align:center;background:rgba(200,200,200,.9);font-weight:700;font-size:13px;color:#333}

  /* footer */
  .footer-rule{left:203px;top:716px;width:797px;height:4px;background:var(--navy)}
  .footer{left:203px;top:722px;width:797px;height:212px;background:var(--gray-bg);display:flex}
  .footer > div{padding:12px 12px 0;border-right:1px solid var(--line)}
  .footer > div:last-child{border-right:none}
  .footer h3{font-size:14px;color:var(--navy);font-weight:700;border-bottom:1px solid var(--line);padding-bottom:6px;margin-bottom:8px}
  .quick{width:230px}
  .field{height:20px;background:var(--white);border:1px solid #ccc;margin-bottom:6px;padding:2px 5px;font-size:9px;color:#999}
  .field.msg{height:70px}
  .quick .btn{float:right;font-size:10px;padding:3px 12px;border-radius:4px;font-family:"Open Sans",sans-serif}
  .services{width:222px}
  .services ul{list-style:none}
  .services li{font-size:9.5px;border-bottom:1px dotted #bbb;padding:2px 0 2px 10px;position:relative}
  .services li::before{content:"";position:absolute;left:0;top:7px;width:4px;height:4px;background:var(--navy)}
  .follow{width:150px}
  .socials{display:flex;gap:14px}
  .social{text-align:center;font-size:9px}
  .social i{display:block;width:40px;height:40px;border-radius:50%;background:var(--navy);margin:0 auto 2px}
  .seal{width:70px;height:70px;border-radius:50%;background:radial-gradient(circle,#e8c850,#b08a1c);margin:16px 0 0 24px}
  .info{flex:1}
  .info p{font-size:9px;margin-bottom:8px}
  .mini-brand{display:flex;align-items:center;gap:8px;margin-top:16px}
  .mini-brand i{width:14px;height:14px;border-radius:50%;background:var(--navy);display:block}
  .mini-brand b{color:var(--navy);font-weight:400;font-size:16px;line-height:1;white-space:nowrap}
  .bottom-band{left:203px;top:937px;width:797px;height:12px;background:var(--navy-dark)}
  .copyright{left:700px;top:966px;width:300px;text-align:right;font-size:9px;color:#666}
</style>
</head>
<body>

<header>
  <nav class="main-nav abs">
    <a class="active" href="#">Home</a><a href="#">Services</a><a href="#">Showcase</a><a href="#">Testimonial</a><a href="#">Contact Us</a>
  </nav>
  <div class="brand abs">
    <span class="brand-dot"></span>
    <span class="brand-name">KTR Builders</span>
  </div>
  <blockquote class="motto abs">"We are what we repeatedly do. Excellence, therefore, is not an act, but a habit."<cite>Theon Varis</cite></blockquote>
  <div class="header-rule abs"></div>
</header>

<section class="slider abs">
  <div class="slide-photo" role="img" aria-label="Bright finished living room with wooden floor, tall windows and red rug"></div>
  <div class="slide-caption abs">
    <h2>Project Name</h2>
    <h3>Vivamus lorem accumsan dolor tempus</h3>
    <p>Sed ut perspiciatis unde omnis iste natus error sit voluptatem accusant doloremque laudantium, totam rem aperiam, eaque ipsa quae ab illo inve tore veritatis architecto.</p>
    <span class="btn">Read More</span>
  </div>
  <div class="dots abs"><i class="on"></i><i></i><i></i><i></i><i></i></div>
</section>

<section class="testimonials abs">
  <h2>Testimonials</h2>
  <p>Nemo enim ipsam voluptatem quia voluptas sit aspernatur aut odit aut fugit, sed quia consequuntur magni dolores eos qui ratione voluptatem sequi nesciunt. Neque porro quisquam est, qui dolorem ipsum quia dolor sit amet, consectetur, adipisci velit, sed quia non numquam eius modi tempora incidunt ut.</p>
  <p class="author">Dale Morwin</p>
</section>

<section class="about abs">
  <h2>KTR Builders INC.</h2>
  <div class="about-img" role="img" aria-label="Architectural drawing of a new custom home"></div>
  <p>Lorem ipsum dolor sit amet, consectetuer adipiscing elit. Aenean massa, parturient montes, nascetur ridiculus, pellentesque eu, pretium quis, sem. Donec quis justo, fringilla vel.</p>
  <p class="hl">In enim justo, rhoncus ut, imperdiet a, felis eu pede mollis pretium.</p>
  <p>Nulla consequat massa quis enim. Donec vulputate eget, arcu. In enim justo, rhoncus ut, imperdiet a, venenatis vitae justo. Lorem ipsum dolor sit amet, consectetur elit. Aenean commodo ligula eget dolor aenean massa penatibus.</p>
</section>

<section class="showcase abs">
  <div class="showcase-img" role="img" aria-label="Showcase interior with red curtains"></div>
  <span>SHOW CASE</span>
</section>

<div class="footer-rule abs"></div>
<footer class="footer abs">
  <div class="quick">
    <h3>Quick Contact:</h3>
    <div class="field">Your Email .....</div>
    <div class="field msg">Your Message .....</div>
    <span class="btn">Submit</span>
  </div>
  <div class="services">
    <h3>Our Services:</h3>
    <ul>
      <li>Vivamus Eget Nisl Nec Trio</li>
      <li>Etiam Cursus Leo Vel</li>
      <li>Metus Nulla Facilisi Etiam</li>
      <li>Aenean Nec Eros Ipsum Prima</li>
      <li>Nelin Nulla Auctor Aenean</li>
      <li>Nec Erat Vestibulum Avis</li>
      <li>Ipsum Primis Faucibus Etiam</li>
      <li>Orci Luctus Et Ultrices Ipsum Primis</li>
    </ul>
  </div>
  <div class="follow">
    <h3>Follow Us:</h3>
    <div class="socials">
      <div class="social"><i></i>Frendo</div>
      <div class="social"><i></i>Chirpa</div>
    </div>
    <div class="seal"></div>
  </div>
  <div class="info">
    <p>Phasellus viverra nulla ut metus varius laoreet. Quisque rutrum. Aenean imperdiet.</p>
    <p>Etiam ultricies nisi vel augue. Curabitur ullamcorper ultricies nisi. Nam eget dui.</p>
    <div class="mini-brand"><i></i><b>KTR Builders</b></div>
  </div>
</footer>
<div class="bottom-band abs"></div>
<p class="copyright abs">© 2011 KTR Builders INC. All rights reserved.</p>

</body>
</html>
```